Marlow Realty Real Estate Brokerage Recruiting Flyer

We are a real estate brokerage looking to hire more real estate agents. We need to list everything we have to offer as a company so real estate agents will join our company. this is our company website: www.Marlowrealty.example .

100% COMMISSION NO MONTHLY FEE
$450 Flat Transaction FEE

What We Offer:
24/7 Office Access
Free E & O Insurance for 1st Year
Free Online CE and PLE
Free 1,000 Business Cards
Free Professional Social Media Marketing
Free Printing, Scanning, and Copies
Free Buyer and Seller Presentation Packages
Free Filquay Cloud Based Document Management Access
Access to our Internal Brokerage Forum
Company Profit Sharing!
Private Offices Available to Rent

*Lead Generation Software with over 3,000 Leads
*10 Leads to Start
* Free Personal CRM and Website
*Restrictions and Rules apply

Company Address:
4817 Amberfield Road
Suite 512
Fairfax, VA 22194
Phone: 703-555-0147
email: info@marlowrealty.example

Target Market(s)

Real Estate Agents

Industry/Entity Type

Real Estate

Colors
0555a3
ffffff

Requirements
Must have
• 100% COMMISSION NO MONTHLY FEE
$450 Flat Transaction FEE

What We Offer:
24/7 Office Access
Free Online CE and PLE
Free 1,000 Business Cards
Company Profit Sharing!

*10 Leads to Start

Company Address:
4817 Amberfield Road
Suite 512
Fairfax, VA 22194
Phone: 703-555-0147

```html
<!DOCTYPE html>
<html lang="en">
<head>
<meta charset="utf-8">
<title>Marlow Realty – Agent Recruiting Flyer</title>
<link rel="stylesheet" href="https://fonts.googleapis.com/css2?family=Lato:wght@400;700;900&display=swap">
<style>
  :root {
    --navy: #0a3170;
    --brand-blue: #0555a3;
    --gold: #e0ae12;
    --gold-soft: #d9a90f;
    --paper: #e8edf4;
    --white: #ffffff;
    --ink: #2a2f3a;
    --footer-grey: #8e9096;
    --stage: #b9bcc9;
  }
  * { box-sizing: border-box; margin: 0; padding: 0; }
  html, body { width: 1200px; height: 1200px; overflow: hidden; }
  body { background: var(--stage); font-family: "Lato", Arial, sans-serif; position: relative; }

  .flyer { position: absolute; left: 191px; top: 60px; width: 856px; height: 1070px; background: var(--paper); overflow: hidden; }
  .flyer-shapes { position: absolute; inset: 0; }

  .brand { position: absolute; right: 36px; top: 62px; width: 260px; text-align: center; color: var(--navy); font-weight: 700; }
  .brand-name { font-size: 42px; letter-spacing: 2px; line-height: 1; display: flex; align-items: center; justify-content: center; gap: 12px; }
  .brand-mark { width: 22px; height: 22px; background: var(--navy); display: inline-block; }
  .brand-sub { font-size: 17px; letter-spacing: 4px; margin-top: 6px; }

  .join { position: absolute; left: 19px; top: 585px; color: var(--gold); font-weight: 700; font-size: 30px; line-height: 37px; }
  .join-rule { position: absolute; left: 0; top: 697px; width: 136px; height: 3px; background: var(--white); }
  .perks { position: absolute; left: 19px; top: 738px; list-style: none; color: var(--white); font-size: 20px; line-height: 25px; }
  .perks .wrap { padding-left: 16px; display: block; }
  .perks .hl { color: var(--gold); }
  .contact-call { position: absolute; left: 22px; top: 926px; color: var(--gold); font-weight: 700; font-size: 20px; line-height: 25px; }

  .offer-title { position: absolute; left: 662px; top: 592px; color: var(--navy); font-weight: 700; font-size: 23px; }
  .offer-rule { position: absolute; left: 661px; top: 621px; width: 195px; height: 3px; background: var(--gold); }
  .offer-list { position: absolute; left: 401px; top: 639px; list-style: none; color: var(--ink); font-size: 19px; line-height: 23.2px; }
  .offer-list li { display: flex; align-items: center; gap: 8px; }
  .offer-list b { color: var(--navy); font-weight: 900; }
  .tick { width: 18px; height: 18px; flex: none; }

  .licence { position: absolute; left: 428px; top: 958px; font-weight: 700; font-size: 15px; color: var(--ink); }
  .badge { position: absolute; }
  .badge-realtor { left: 742px; top: 933px; width: 38px; height: 40px; background: var(--brand-blue); }
  .badge-housing { left: 792px; top: 930px; width: 46px; height: 46px; border: 4px solid #111; background: var(--white); }

  .footer-text { position: absolute; color: var(--white); font-size: 18px; line-height: 26px; white-space: nowrap; }
  .addr { left: 47px; top: 1003px; }
  .phone-mail { left: 328px; top: 1003px; font-size: 17px; }
  .web { left: 570px; top: 1025px; font-weight: 700; font-size: 18px; }
  .icon { position: absolute; }
  .social-square { position: absolute; left: 812px; top: 1022px; width: 30px; height: 30px; background: var(--white); border-radius: 3px; }
</style>
</head>
<body>
<main class="flyer">
  <svg class="flyer-shapes" width="856" height="1070" viewBox="0 0 856 1070">
    <defs>
      <linearGradient id="teamPhotoTone" x1="0" y1="0" x2="1" y2="1">
        <stop offset="0" stop-color="#dfe3e8"/>
        <stop offset="0.5" stop-color="#c9c5bf"/>
        <stop offset="1" stop-color="#5d6270"/>
      </linearGradient>
    </defs>
    <rect class="top-strip" x="0" y="0" width="856" height="13" fill="var(--gold)"/>
    <rect x="0" y="13" width="856" height="500" fill="#f3f5f8"/>
    <rect class="team-photo" x="102" y="13" width="640" height="470" fill="url(#teamPhotoTone)" role="img" aria-label="Photo of four smiling real estate agents raising their fists in celebration"/>
    <polygon class="logo-panel" points="505,13 856,13 856,195 545,122" fill="var(--white)"/>
    <polygon class="gold-wedge" points="0,355 175,470 0,500" fill="var(--gold-soft)"/>
    <polygon class="gold-band" points="0,495 856,350 856,500 369,602" fill="var(--gold)"/>
    <polygon class="navy-panel" points="0,500 369,602 289,988 0,988" fill="var(--navy)"/>
    <rect class="footer-bar" x="0" y="988" width="856" height="82" fill="var(--footer-grey)"/>
    <polygon class="footer-navy" points="544,988 856,988 856,1070 506,1070" fill="var(--navy)"/>

    <g transform="translate(207,527) rotate(-10.5)" font-family="Lato, Arial, sans-serif">
      <text class="headline" x="0" y="0" font-size="70" font-weight="900" fill="var(--white)" textLength="625" lengthAdjust="spacingAndGlyphs">100% COMMISSION</text>
      <text x="285" y="44" font-size="34" font-weight="700" fill="var(--white)" textLength="318" lengthAdjust="spacingAndGlyphs">NO MONTHLY FEE</text>
      <rect x="285" y="56" width="362" height="3" fill="var(--white)"/>
      <text x="203" y="92" font-size="29" font-weight="900" fill="var(--navy)" textLength="365" lengthAdjust="spacingAndGlyphs">$450 Flat Transaction FEE</text>
    </g>
  </svg>

  <div class="brand">
    <div class="brand-name"><span class="brand-mark"></span>MARLOW</div>
    <div class="brand-sub">Realty</div>
  </div>

  <h2 class="join">JOIN<br>OUR WINNING TEAM<br>TODAY!</h2>
  <div class="join-rule"></div>
  <ul class="perks">
    <li>* Lead Generation Software<span class="wrap">with over 3,000 Leads</span></li>
    <li>* 10 Leads to Start</li>
    <li>* <span class="hl">FREE</span> Personal CRM and<span class="wrap">Website</span></li>
    <li>* Restrictions and Rules apply</li>
  </ul>
  <p class="contact-call">GET IN TOUCH WITH US<br>FOR MORE INFO:</p>

  <h3 class="offer-title">What We Offer:</h3>
  <div class="offer-rule"></div>
  <ul class="offer-list">
    <li><svg class="tick" viewBox="0 0 18 18"><circle cx="9" cy="9" r="7.5" fill="none" stroke="var(--gold)" stroke-width="1.6"/><path d="M5 9l3 3 8-8" fill="none" stroke="var(--gold)" stroke-width="2"/></svg><span><b>24/7</b> Office Access</span></li>
    <li><svg class="tick" viewBox="0 0 18 18"><circle cx="9" cy="9" r="7.5" fill="none" stroke="var(--gold)" stroke-width="1.6"/><path d="M5 9l3 3 8-8" fill="none" stroke="var(--gold)" stroke-width="2"/></svg><span><b>FREE</b> E &amp; O Insurance for 1st Year</span></li>
    <li><svg class="tick" viewBox="0 0 18 18"><circle cx="9" cy="9" r="7.5" fill="none" stroke="var(--gold)" stroke-width="1.6"/><path d="M5 9l3 3 8-8" fill="none" stroke="var(--gold)" stroke-width="2"/></svg><span><b>FREE</b> Online CE and PLE</span></li>
    <li><svg class="tick" viewBox="0 0 18 18"><circle cx="9" cy="9" r="7.5" fill="none" stroke="var(--gold)" stroke-width="1.6"/><path d="M5 9l3 3 8-8" fill="none" stroke="var(--gold)" stroke-width="2"/></svg><span><b>FREE</b> 1,000 Business Cards</span></li>
    <li><svg class="tick" viewBox="0 0 18 18"><circle cx="9" cy="9" r="7.5" fill="none" stroke="var(--gold)" stroke-width="1.6"/><path d="M5 9l3 3 8-8" fill="none" stroke="var(--gold)" stroke-width="2"/></svg><span><b>FREE</b> Professional Social Media Marketing</span></li>
    <li><svg class="tick" viewBox="0 0 18 18"><circle cx="9" cy="9" r="7.5" fill="none" stroke="var(--gold)" stroke-width="1.6"/><path d="M5 9l3 3 8-8" fill="none" stroke="var(--gold)" stroke-width="2"/></svg><span><b>FREE</b> Printing, Scanning, and Copies</span></li>
    <li><svg class="tick" viewBox="0 0 18 18"><circle cx="9" cy="9" r="7.5" fill="none" stroke="var(--gold)" stroke-width="1.6"/><path d="M5 9l3 3 8-8" fill="none" stroke="var(--gold)" stroke-width="2"/></svg><span><b>FREE</b> Buyer and Seller Presentation Packages</span></li>
    <li><svg class="tick" viewBox="0 0 18 18"><circle cx="9" cy="9" r="7.5" fill="none" stroke="var(--gold)" stroke-width="1.6"/><path d="M5 9l3 3 8-8" fill="none" stroke="var(--gold)" stroke-width="2"/></svg><span><b>FREE</b> Filquay Cloud Based Document</span></li>
    <li><svg class="tick" viewBox="0 0 18 18"><circle cx="9" cy="9" r="7.5" fill="none" stroke="var(--gold)" stroke-width="1.6"/><path d="M5 9l3 3 8-8" fill="none" stroke="var(--gold)" stroke-width="2"/></svg><span>Management Access</span></li>
    <li><svg class="tick" viewBox="0 0 18 18"><circle cx="9" cy="9" r="7.5" fill="none" stroke="var(--gold)" stroke-width="1.6"/><path d="M5 9l3 3 8-8" fill="none" stroke="var(--gold)" stroke-width="2"/></svg><span>Access to our Internal Brokerage Forum</span></li>
    <li><svg class="tick" viewBox="0 0 18 18"><circle cx="9" cy="9" r="7.5" fill="none" stroke="var(--gold)" stroke-width="1.6"/><path d="M5 9l3 3 8-8" fill="none" stroke="var(--gold)" stroke-width="2"/></svg><span>Company Profit Sharing!</span></li>
    <li><svg class="tick" viewBox="0 0 18 18"><circle cx="9" cy="9" r="7.5" fill="none" stroke="var(--gold)" stroke-width="1.6"/><path d="M5 9l3 3 8-8" fill="none" stroke="var(--gold)" stroke-width="2"/></svg><span>Private Offices Available to Rent</span></li>
  </ul>

  <p class="licence">LICENSED DC. MARYLAND, VIRGINIA.</p>
  <div class="badge badge-realtor"></div>
  <div class="badge badge-housing"></div>

  <svg class="icon" style="left:24px;top:1004px" width="20" height="26" viewBox="0 0 20 26"><path d="M10 1a8 8 0 0 0-8 8c0 6 8 16 8 16s8-10 8-16a8 8 0 0 0-8-8z" fill="var(--navy)"/><circle cx="10" cy="9" r="3" fill="var(--footer-grey)"/></svg>
  <p class="footer-text addr">4817 Amberfield Road<br>Suite 512, Fairfax, VA 22194</p>

  <svg class="icon" style="left:301px;top:1007px" width="20" height="20" viewBox="0 0 20 20"><path d="M4 2l4 1 1 4-2 2a11 11 0 0 0 4 4l2-2 4 1 1 4-2 2C9 18 2 11 2 4z" fill="none" stroke="var(--navy)" stroke-width="1.8"/></svg>
  <svg class="icon" style="left:301px;top:1035px" width="20" height="16" viewBox="0 0 20 16"><rect x="1" y="1" width="18" height="14" fill="none" stroke="var(--navy)" stroke-width="1.6"/><path d="M1 1l9 8 9-8" fill="none" stroke="var(--navy)" stroke-width="1.6"/></svg>
  <p class="footer-text phone-mail">703-555-0147<br>info@marlowrealty.example</p>

  <svg class="icon" style="left:542px;top:1027px" width="22" height="22" viewBox="0 0 22 22"><circle cx="11" cy="11" r="9" fill="none" stroke="var(--gold)" stroke-width="2"/><ellipse cx="11" cy="11" rx="4" ry="9" fill="none" stroke="var(--gold)" stroke-width="1.6"/><path d="M2 11h18M4 6h14M4 16h14" stroke="var(--gold)" stroke-width="1.4"/></svg>
  <p class="footer-text web">www.Marlowrealty.example</p>
  <div class="social-square"></div>
</main>
</body>
</html>
```